VELORA ARENA CHANNEL-Where being an athlete is a STATE OF MIND-NOT A GENDER

WEBSITE AND OTT NETWORK DEDICATED TO WOMENS SPORTS
VELORA ARENA CHANNEL intends to address the needs of this underserved market in women’s sports media coverage by uniquely delivering 24/7 focused coverage to those interested specifically in women’s sports and related stories, in a more direct and customer driven way.

Our product provides the following solutions:
1. Provides programming to an underserved market
2. Provides expansive exposure (a critical ingredient) for the success of professional women’s sports
3. Values the athletic achievement of female athletes

This will be accomplished in two phases:
Phase 1
Create a dynamic website dedicated to women’s sports featuring up to date scores, highlights and news.
Phase 2
1. Create a full-spectrum OTT (over the top) network that reflects the dynamic and changing nature of women’s athletics, providing innovative programming, helpful information, community and individual experiences, entertainment and a touch of much-needed humor.
2. Create a network dedicated to women’s sports and entertainment that features steady rotation of daily news and highlights of women’s sports delivered by a majority of women reporters. A sports channel for women by women.
3. To offer live, pre-taped, original and diverse programming 24 hours a day seven days a week, 365 days a year.

VVELORA ARENA CHANNEL website “ Veloratv.net “ fills a need to help women’s sports and entertainment enthusiasts get the complete array of scores and highlights they are craving to make the most of their viewing time online. Stats
So VeloraTV.net plans to go above and beyond what the current sports driven websites offer. But beyond what we will offer the consumer, we are also providing an incredible platform for women in sports to showcase their talent to a starved underserved crowd of sports fans.
No matter what your age or skill level or even education, people are searching the web to find specific information, products, and services that interest them. Recognizing the magnitude of our target market that are searching the Internet for various information we realize the importance of meeting their needs with opportunities to discover who we are and what we do. With every search, every click and every download we will be able to get one step closer to our target market.

Target Market(s)

people interested in womens sports

Number of Pages Required

4 page

Font styles to use
Serif

Requirements
Must have
• home page design exactly like www.brisklanegames.net and the ott page (watch page) similar to streamora page, all with womens sports in mind
Nice to have
• view brisklanegames and streamora. Color coordinate to logo

```html
<!DOCTYPE html>
<html lang="en">
<head>
<meta charset="utf-8">
<title>Velora Arena Channel</title>
<link href="https://fonts.googleapis.com/css2?family=Open+Sans:wght@400;600;700&family=Oswald:wght@500;600&display=swap" rel="stylesheet">
<style>
:root{
  --red:#e0402b;
  --red-dark:#b92d1c;
  --ink:#222;
  --text:#666;
  --muted:#999;
  --line:#e3e3e3;
  --band:#f0f0f0;
  --black:#111;
  --white:#fff;
}
*{box-sizing:border-box;margin:0;padding:0}
html,body{width:1200px;height:2388px;overflow:hidden}
body{font-family:"Open Sans",Arial,sans-serif;color:var(--text);background:var(--white);position:relative}
.container{width:1008px;margin:0 auto}

/* hero + header */
.hero{position:relative;height:664px;background:linear-gradient(160deg,#3d4a3a 0%,#6f7a5c 35%,#b8b0a4 55%,#5a4f4a 80%,#222 100%)}
.topbar{position:absolute;left:0;right:0;top:0;height:44px;background:rgba(0,0,0,.85)}
.brand{position:absolute;left:84px;top:10px;display:flex;align-items:center;gap:10px;background:var(--white);padding:14px 16px;height:100px;width:220px;box-shadow:0 2px 6px rgba(0,0,0,.3)}
.brand-dot{width:34px;height:34px;border-radius:50%;background:var(--red);flex:none}
.brand-name{font-weight:700;font-size:18px;line-height:1.15;color:var(--red)}
.account{position:absolute;right:56px;top:12px;display:flex;gap:22px;font-size:14px;color:var(--white)}
.account span::before{content:"";display:inline-block;width:10px;height:10px;border-radius:50%;background:var(--white);margin-right:7px;vertical-align:-1px}
.search{position:absolute;right:48px;top:60px;width:260px;height:32px;background:#1b1b1b;border:1px solid #444;color:#bbb;font-size:14px;padding:6px 12px}
.search svg{position:absolute;right:9px;top:8px}
.mainnav{position:absolute;left:320px;right:0;top:104px;height:42px;background:var(--red);display:flex;align-items:center;padding-left:4px}
.mainnav a{color:var(--white);text-decoration:none;font-size:14px;font-weight:600;padding:0 16px;height:32px;line-height:32px}
.mainnav a.active{background:var(--red-dark);border-radius:3px}
.slide-arrow{position:absolute;top:384px;width:30px;height:30px;border-radius:50%;background:rgba(0,0,0,.55)}
.slide-arrow.left{left:12px}.slide-arrow.right{right:12px}
.slide-arrow svg{position:absolute;left:9px;top:8px}
.caption{position:absolute;left:0;right:0;bottom:0;height:64px;background:rgba(0,0,0,.75);text-align:center;font-family:"Oswald",Arial,sans-serif;font-weight:500;font-size:30px;color:var(--white);line-height:64px}

/* about */
.about{text-align:center;padding-top:66px}
.about h2{display:inline-flex;align-items:center;gap:12px;font-size:32px;font-weight:600;color:#444;letter-spacing:1px}
.about h2 .accent{color:var(--red)}
.about h2::before,.about h2::after{content:"";width:240px;height:1px;background:var(--line)}
.about p{margin:18px auto 0;width:1000px;font-size:13px;line-height:22px;color:var(--text)}

/* filters */
.filters{margin-top:48px;height:44px;background:var(--band);display:flex;align-items:center;padding-left:14px;gap:30px;font-size:13px;font-weight:700;color:#444}
.filters .all{color:var(--red)}
.filters .tag::before{content:"+ ";color:var(--red)}

/* banner */
.promo{margin-top:28px;height:160px;position:relative;background:#1a1a1a;overflow:hidden}
.promo-photo{position:absolute;left:0;top:0;width:560px;height:100%;background:linear-gradient(90deg,#2b2f3a,#6b4a3a 40%,#a2553d 60%,#2a2a2a)}
.promo-logo{position:absolute;left:20px;top:58px;display:flex;align-items:center;gap:8px;font-weight:700;font-size:26px;color:var(--white)}
.promo-logo i{width:20px;height:20px;background:var(--red);display:block}
.promo-right{position:absolute;left:660px;top:22px;right:40px;text-align:center;color:var(--white)}
.promo-right .name{font-family:"Oswald",Arial,sans-serif;font-size:24px;letter-spacing:2px}
.promo-right .role{font-size:13px;letter-spacing:3px;margin-top:2px}
.promo-right .cta{display:inline-block;margin-top:14px;background:var(--red);padding:8px 22px;font-size:14px;line-height:18px}

/* cards */
.cards{margin-top:42px;display:grid;grid-template-columns:repeat(4,234px);column-gap:24px;row-gap:28px}
.card{border-bottom:3px solid var(--red);padding-bottom:12px;height:282px}
.card-photo{position:relative;height:124px}
.card-tag{position:absolute;left:0;bottom:0;background:rgba(0,0,0,.75);color:var(--white);font-size:11px;font-weight:700;padding:4px 8px}
.card h3{margin-top:12px;font-size:14px;line-height:18px;color:var(--red);font-weight:700}
.card p{margin-top:8px;font-size:12px;line-height:17px;color:var(--text)}
.ph-bball{background:linear-gradient(135deg,#c96a2c,#5d3b6b)}
.ph-hockey{background:linear-gradient(135deg,#3e7a3c,#a9c48d)}
.ph-soccer{background:linear-gradient(135deg,#2f5aa8,#c8c8c8)}
.ph-tennis{background:linear-gradient(135deg,#3f6b3a,#9ec48a)}

/* bottom columns */
.feeds{margin-top:42px;display:grid;grid-template-columns:472px 472px;column-gap:64px}
.feed-title{display:flex;align-items:center;gap:10px;font-size:18px;font-weight:700;color:#333;border-bottom:1px solid var(--line);padding-bottom:10px}
.feed-title i{width:24px;height:24px;border-radius:4px;background:#333;display:block}
.feed-title i.blue{background:#2a9fd8;border-radius:50%}
.news{display:flex;gap:14px;margin-top:20px}
.date{width:54px;height:54px;background:var(--red);color:var(--white);text-align:center;flex:none;font-weight:700;font-size:20px;line-height:24px;padding-top:5px}
.date small{display:block;font-size:11px;line-height:16px}
.news h4{font-size:13px;color:var(--ink)}
.news p{font-size:12px;line-height:17px;margin-top:3px}
.tweet{display:flex;gap:16px;margin-top:22px}
.avatar{width:80px;height:80px;flex:none;background:linear-gradient(135deg,#b88a6e,#4c3a33)}
.tweet-body{flex:1}
.tweet-head{display:flex;justify-content:space-between;font-size:12px}
.tweet-head b{color:var(--ink)}
.tweet-head span{color:var(--muted)}
.tweet p{font-size:12px;line-height:17px;margin-top:4px}

/* footer */
.footer{position:absolute;left:0;right:0;bottom:0;height:78px;background:var(--red);color:var(--white)}
.footer-links{position:absolute;left:96px;top:16px;font-size:13px}
.footer-links span{margin:0 6px}
.copyright{position:absolute;left:96px;top:44px;font-size:12px;opacity:.9}
.footer-mark{position:absolute;left:780px;top:14px;width:50px;height:50px;border-radius:50%;background:rgba(255,255,255,.35)}
.social{position:absolute;right:96px;top:22px;display:flex;gap:10px}
.social i{width:32px;height:32px;border-radius:50%;border:2px solid var(--white);display:block}
</style>
</head>
<body>

<header class="hero" role="img" aria-label="Action photo of a women's football match, player sliding for the ball">
  <div class="topbar"></div>
  <div class="brand"><span class="brand-dot"></span><span class="brand-name">VELORA ARENA CHANNEL</span></div>
  <div class="account"><span>Login</span><span>Register</span></div>
  <div class="search">Search
    <svg width="14" height="14" viewBox="0 0 14 14"><circle cx="6" cy="6" r="4.5" fill="none" stroke="#bbb" stroke-width="1.6"/><line x1="9.4" y1="9.4" x2="13" y2="13" stroke="#bbb" stroke-width="1.6"/></svg>
  </div>
  <nav class="mainnav">
    <a class="active">HOME</a><a>ABOUT US</a><a>PROGRAMS</a><a>SPORTS</a><a>SCHEDULE</a><a>TOP STORIES</a><a>BLOG</a><a>CONTACT US</a>
  </nav>
  <span class="slide-arrow left"><svg width="12" height="14" viewBox="0 0 12 14"><path d="M9 1 3 7l6 6" fill="none" stroke="#fff" stroke-width="2"/></svg></span>
  <span class="slide-arrow right"><svg width="12" height="14" viewBox="0 0 12 14"><path d="M3 1l6 6-6 6" fill="none" stroke="#fff" stroke-width="2"/></svg></span>
  <div class="caption">Providing expansive exposure for the success of professional women's sports</div>
</header>

<main class="container">
  <section class="about">
    <h2>ABOUT <span class="accent">VELORA</span></h2>
    <p>Lorem ipsum dolor sit amet, consectetuer adipiscing elit, sed diam nonummy nibh euismod tincidunt ut laoreet dolore magna aliquam erat volutpat. Ut wisi enim ad minim veniam, quis nostrud exerci tation ullamcorper suscipit lobortis nisl ut aliquip ex ea commodo consequat. Duis autem vel eum iriure dolor in hendrerit in vulputate velit esse molestie consequat, vel illum dolore eu feugiat nulla facilisis at vero eros et accumsan et iusto odio dignissim qui blandit praesent luptatum.</p>
  </section>

  <div class="filters"><span class="all">ALL</span><span class="tag">BASKETBALL</span><span class="tag">HOCKEY</span><span class="tag">SOCCER</span><span class="tag">TENNIS</span><span class="tag">VOLLEYBALL</span></div>

  <section class="promo">
    <div class="promo-photo" role="img" aria-label="Sportswear advertisement photo of a surfer and products"></div>
    <div class="promo-logo"><i></i>STRIDE</div>
    <div class="promo-right">
      <div class="name">MARISOL KEANE</div>
      <div class="role">WOMEN ATHLETE</div>
      <div class="cta">Lorem ipsum dolor sit amet<br>consectetuer adipiscing</div>
    </div>
  </section>

  <section class="cards">
    <article class="card"><div class="card-photo ph-bball" role="img" aria-label="Women's basketball game photo"><span class="card-tag">BASKETBALL</span></div><h3>Lorem ipsum dolor sit amet consectetuer adipiscing</h3><p>Lorem ipsum dolor sit amet, sed diam nibh euismod tincidunt ut laoreet dolore magna aliquam erat volutpat ut wisi enim ad minim veniam.</p></article>
    <article class="card"><div class="card-photo ph-hockey" role="img" aria-label="Women's field hockey match photo"><span class="card-tag">HOCKEY</span></div><h3>Lorem ipsum dolor sit amet consectetuer adipiscing</h3><p>Lorem ipsum dolor sit amet, sed diam nibh euismod tincidunt ut laoreet dolore magna aliquam erat volutpat ut wisi enim ad minim veniam.</p></article>
    <article class="card"><div class="card-photo ph-soccer" role="img" aria-label="Women's soccer match photo"><span class="card-tag">SOCCER</span></div><h3>Lorem ipsum dolor sit amet consectetuer adipiscing</h3><p>Lorem ipsum dolor sit amet, sed diam nibh euismod tincidunt ut laoreet dolore magna aliquam erat volutpat ut wisi enim ad minim veniam.</p></article>
    <article class="card"><div class="card-photo ph-tennis" role="img" aria-label="Women's tennis player on court photo"><span class="card-tag">TENNIS</span></div><h3>Lorem ipsum dolor sit amet consectetuer adipiscing</h3><p>Lorem ipsum dolor sit amet, sed diam nibh euismod tincidunt ut laoreet dolore magna aliquam erat volutpat ut wisi enim ad minim veniam.</p></article>
    <article class="card"><div class="card-photo ph-bball" role="img" aria-label="Women's basketball drive to the hoop photo"><span class="card-tag">BASKETBALL</span></div><h3>Lorem ipsum dolor sit amet consectetuer adipiscing</h3><p>Lorem ipsum dolor sit amet, sed diam nibh euismod tincidunt ut laoreet dolore magna aliquam erat volutpat ut wisi enim ad minim veniam.</p></article>
    <article class="card"><div class="card-photo ph-hockey" role="img" aria-label="Women's hockey players on the field photo"><span class="card-tag">HOCKEY</span></div><h3>Lorem ipsum dolor sit amet consectetuer adipiscing</h3><p>Lorem ipsum dolor sit amet, sed diam nibh euismod tincidunt ut laoreet dolore magna aliquam erat volutpat ut wisi enim ad minim veniam.</p></article>
    <article class="card"><div class="card-photo ph-soccer" role="img" aria-label="Women's soccer celebration photo"><span class="card-tag">SOCCER</span></div><h3>Lorem ipsum dolor sit amet consectetuer adipiscing</h3><p>Lorem ipsum dolor sit amet, sed diam nibh euismod tincidunt ut laoreet dolore magna aliquam erat volutpat ut wisi enim ad minim veniam.</p></article>
    <article class="card"><div class="card-photo ph-tennis" role="img" aria-label="Women's tennis serve photo"><span class="card-tag">TENNIS</span></div><h3>Lorem ipsum dolor sit amet consectetuer adipiscing</h3><p>Lorem ipsum dolor sit amet, sed diam nibh euismod tincidunt ut laoreet dolore magna aliquam erat volutpat ut wisi enim ad minim veniam.</p></article>
  </section>

  <section class="feeds">
    <div>
      <div class="feed-title"><i></i>LATEST NEWS</div>
      <div class="news"><div class="date">04<small>JAN</small></div><div><h4>Lorem ipsum dolor sit amet nisi</h4><p>Lorem ipsum dolor sit amet, consectetuer adipiscing elit, sed diam nonummy nibh euismod tincidunt ut laoreet dolore.</p></div></div>
      <div class="news"><div class="date">04<small>JAN</small></div><div><h4>Lorem ipsum dolor sit amet nisi</h4><p>Lorem ipsum dolor sit amet, consectetuer adipiscing elit, sed diam nonummy nibh euismod tincidunt ut laoreet dolore.</p></div></div>
      <div class="news"><div class="date">04<small>JAN</small></div><div><h4>Lorem ipsum dolor sit amet nisi</h4><p>Lorem ipsum dolor sit amet, consectetuer adipiscing elit, sed diam nonummy nibh euismod tincidunt ut laoreet dolore.</p></div></div>
    </div>
    <div>
      <div class="feed-title"><i class="blue"></i>CHIRPER FEED</div>
      <div class="tweet"><div class="avatar" role="img" aria-label="Profile photo"></div><div class="tweet-body"><div class="tweet-head"><b>@VELORATVSPORTS</b><span>12 hours ago</span></div><p>Lorem ipsum dolor sit amet, consectetuer adipiscing elit, sed diam nonummy nibh euismod tincidunt ut laoreet dolore magna aliquam erat.</p></div></div>
      <div class="tweet"><div class="avatar" role="img" aria-label="Profile photo"></div><div class="tweet-body"><div class="tweet-head"><b>@VELORATVSPORTS</b><span>12 hours ago</span></div><p>Lorem ipsum dolor sit amet, consectetuer adipiscing elit, sed diam nonummy nibh euismod tincidunt ut laoreet dolore magna aliquam erat.</p></div></div>
    </div>
  </section>
</main>

<footer class="footer">
  <div class="footer-links">Home<span>|</span>About Us<span>|</span>Programs<span>|</span>Sports<span>|</span>Schedule<span>|</span>Top Stories<span>|</span>Blog<span>|</span>Contact Us</div>
  <div class="copyright">© 2015 Veloratv.net All Rights Reserved.</div>
  <span class="footer-mark"></span>
  <div class="social"><i></i><i></i><i></i><i></i></div>
</footer>

</body>
</html>
```